Velocity Pulse sharing solutions, we offer different types of mobile charging stations for all ty

I need an app that shows all the locations that use our charging stations.
the app should show the following:

1. a map where client can see where all the stations are
2. a map that shows which one is the nearest charging station based on the persons location
3. a search tab where you can pick the city ( all will be based from sweden) and we will start with two cities: Gothenburg and Stockholm. So user will be able to pick the city and than get a list of all venues using our stations. along the way we will keep adding cities and countries but for now i need a design, something i can show potential customers on a power point how this app will work.
4. a list of different venue categories:
- restaurant
- café
- Festival
- Airport
- Library
- Night club
- Shopping center

Once client chooses the city, they can also choose what they are looking for and choose for example which restaurant to eat at based on if they have our charging station or not

you can of course improvise on ideas, if you come up with something and want to add to the app design thats ok, I'm up for suggestions.

in conclusion: the purpose for the app is for users to be able to search for charging stations or see where the nearest charging station is

Target Market(s)

Everyone

Requirements
Must have
• professional and simple design

```html
<!DOCTYPE html>
<html lang="en">
<head>
<meta charset="utf-8">
<title>Velocity Pulse – Pick a Venue</title>
<link rel="stylesheet" href="https://fonts.googleapis.com/css2?family=Source+Sans+3:wght@400;600&display=swap">
<style>
  :root {
    --bg: #2e3350;
    --tile: #0090d0;
    --tile-shadow: rgba(10, 14, 35, 0.45);
    --white: #ffffff;
    --check: #4cd660;
    --back-bg: #f1f1f1;
    --back-text: #6f6f6f;
    --search-bg: #4cd660;
  }
  * { margin: 0; padding: 0; box-sizing: border-box; }
  html, body { width: 675px; height: 1200px; overflow: hidden; background: var(--bg); }
  body { font-family: "Source Sans 3", "Helvetica Neue", Arial, sans-serif; color: var(--white); }

  .screen { position: relative; width: 675px; height: 1200px; background: var(--bg); }

  .status-bar {
    position: absolute; top: 0; left: 0; right: 0; height: 36px;
    display: flex; align-items: center; justify-content: space-between;
    padding: 0 8px; font-size: 18px; font-weight: 400;
  }
  .status-left, .status-right { display: flex; align-items: center; gap: 6px; }
  .status-time { position: absolute; left: 0; right: 0; text-align: center; font-weight: 600; }

  .page-title {
    position: absolute; top: 158px; left: 0; right: 0;
    text-align: center; font-size: 38px; font-weight: 400; line-height: 52px;
  }

  .venue-tile {
    position: absolute; width: 186px; height: 189px;
    background: var(--tile);
    box-shadow: 0 10px 26px var(--tile-shadow);
    border-radius: 2px;
    text-align: center;
  }
  .venue-icon {
    position: absolute; left: 50%; top: 76px; transform: translate(-50%, -50%);
    width: 60px; height: 60px;
  }
  .venue-label {
    position: absolute; left: 0; right: 0; top: 140px; transform: translateY(-50%);
    font-size: 29px; line-height: 38px;
  }
  .venue-label.two-line { top: 148px; }
  .selected-mark { position: absolute; left: 144px; top: 11px; width: 31px; height: 31px; }

  .col-1 { left: 43px; } .col-2 { left: 245px; } .col-3 { left: 447px; }
  .row-1 { top: 341px; } .row-2 { top: 549px; } .row-3 { top: 757px; }

  .action-bar {
    position: absolute; left: 43px; top: 1060px; width: 587px; height: 65px;
    display: flex; border-radius: 33px; overflow: hidden;
  }
  .action-button {
    display: flex; align-items: center; justify-content: center;
    font-size: 31px; font-family: inherit; border: 0;
  }
  .back-button { width: 306px; background: var(--back-bg); color: var(--back-text); }
  .search-button { flex: 1; background: var(--search-bg); color: var(--white); }
</style>
</head>
<body>
<main class="screen">
  <header class="status-bar">
    <div class="status-left">
      <svg width="60" height="10" viewBox="0 0 60 10" aria-hidden="true">
        <g fill="#fff"><circle cx="5" cy="5" r="4.5"/><circle cx="17" cy="5" r="4.5"/><circle cx="29" cy="5" r="4.5"/><circle cx="41" cy="5" r="4.5"/><circle cx="53" cy="5" r="4.5"/></g>
      </svg>
      <span>Nordtel</span>
      <svg width="20" height="15" viewBox="0 0 20 15" aria-hidden="true">
        <path d="M10 14 L6.5 10 A5 5 0 0 1 13.5 10 Z" fill="#fff"/>
        <path d="M3.5 7 A9 9 0 0 1 16.5 7" fill="none" stroke="#fff" stroke-width="2.2"/>
        <path d="M0.8 4 A13 13 0 0 1 19.2 4" fill="none" stroke="#fff" stroke-width="2.2"/>
      </svg>
    </div>
    <span class="status-time">9:41 AM</span>
    <div class="status-right">
      <span>100%</span>
      <svg width="44" height="18" viewBox="0 0 44 18" aria-hidden="true">
        <rect x="0.75" y="0.75" width="38" height="16.5" rx="3.5" fill="none" stroke="#fff" stroke-width="1.5"/>
        <rect x="3" y="3" width="33.5" height="12" rx="1.5" fill="#fff"/>
        <rect x="40.5" y="6" width="2.5" height="6" rx="1" fill="#fff"/>
      </svg>
    </div>
  </header>

  <h1 class="page-title">Please Pick The Venue You<br>Want To Visit</h1>

  <section class="venue-grid">
    <div class="venue-tile col-1 row-1">
      <svg class="venue-icon" viewBox="0 0 60 60" aria-hidden="true" fill="none" stroke="#fff" stroke-width="1.8">
        <ellipse cx="21" cy="45" rx="5" ry="4"/><ellipse cx="37" cy="42" rx="5" ry="4"/>
        <path d="M26 45 V16 L42 12 V42"/><path d="M26 23 L42 19"/>
      </svg>
      <svg class="selected-mark" viewBox="0 0 31 31" aria-hidden="true"><circle cx="15.5" cy="15.5" r="15.5" fill="var(--check)"/><path d="M9 16 L13.5 20.5 L22 11.5" fill="none" stroke="#fff" stroke-width="3" stroke-linecap="round" stroke-linejoin="round"/></svg>
      <span class="venue-label">Night Club</span>
    </div>

    <div class="venue-tile col-2 row-1">
      <svg class="venue-icon" viewBox="0 0 60 60" aria-hidden="true">
        <g fill="none" stroke="#fff" stroke-width="1.6"><path d="M22 8 q3 3 0 6 q-3 3 0 6"/><path d="M29 6 q3 3 0 6 q-3 3 0 6"/><path d="M36 8 q3 3 0 6 q-3 3 0 6"/></g>
        <path d="M14 24 H44 V36 Q44 46 34 46 H24 Q14 46 14 36 Z" fill="#fff"/>
        <path d="M44 28 Q52 28 51 34 Q50 40 43 40" fill="none" stroke="#fff" stroke-width="3.5"/>
        <path d="M6 49 H54 Q50 54 42 54 H18 Q10 54 6 49 Z" fill="#fff"/>
      </svg>
      <span class="venue-label">Café</span>
    </div>

    <div class="venue-tile col-3 row-1">
      <svg class="venue-icon" viewBox="0 0 60 60" aria-hidden="true" fill="none" stroke="#fff" stroke-width="1.8" stroke-linejoin="round">
        <path d="M19 16 L35 12 L41 15 V47 L25 51 L19 48 Z"/><path d="M19 16 L25 19 L41 15"/><path d="M25 19 V51"/>
      </svg>
      <svg class="selected-mark" viewBox="0 0 31 31" aria-hidden="true"><circle cx="15.5" cy="15.5" r="15.5" fill="var(--check)"/><path d="M9 16 L13.5 20.5 L22 11.5" fill="none" stroke="#fff" stroke-width="3" stroke-linecap="round" stroke-linejoin="round"/></svg>
      <span class="venue-label">Library</span>
    </div>

    <div class="venue-tile col-1 row-2">
      <svg class="venue-icon" viewBox="0 0 80 60" aria-hidden="true" style="width:80px" fill="none" stroke="#fff" stroke-width="1.4" stroke-linejoin="round">
        <path d="M2 34 Q30 44 72 22"/><path d="M10 38 Q30 46 74 36"/>
        <path d="M8 35 l3 7 l4 -5"/><path d="M18 38 l2 7 l5 -5"/><path d="M29 40 l2 7 l5 -6"/><path d="M42 39 l2 7 l4 -7"/>
        <path d="M54 34 l2 7 l5 -8"/><path d="M64 29 l4 6 l3 -9"/><path d="M68 25 l4 -8 l2 7"/>
        <path d="M58 30 l3 -8 l4 5"/><path d="M46 35 l1 -8 l5 4"/>
      </svg>
      <span class="venue-label">Festival</span>
    </div>

    <div class="venue-tile col-2 row-2">
      <svg class="venue-icon" viewBox="0 0 60 60" aria-hidden="true" fill="none" stroke="#fff" stroke-width="1.8" stroke-linejoin="round">
        <path d="M13 28 Q13 14 30 14 Q47 14 47 28 Z"/>
        <path d="M11 32 H49"/><path d="M13 36 l4 -3 l4 3 l4 -3 l4 3 l4 -3 l4 3 l4 -3 l4 3"/>
        <path d="M12 40 H48 V43 Q48 46 44 46 H16 Q12 46 12 43 Z"/>
        <circle cx="27" cy="20" r="0.8" fill="#fff"/><circle cx="33" cy="19" r="0.8" fill="#fff"/>
      </svg>
      <span class="venue-label">Restaurant</span>
    </div>

    <div class="venue-tile col-3 row-2">
      <svg class="venue-icon" viewBox="0 0 60 60" aria-hidden="true" fill="none" stroke="#fff" stroke-width="1.8" stroke-linejoin="round">
        <path d="M24 18 V13 H36 V18"/><rect x="9" y="18" width="42" height="29" rx="3"/>
        <path d="M18 18 V47 M42 18 V47 M21 18 V47 M39 18 V47"/>
      </svg>
      <svg class="selected-mark" viewBox="0 0 31 31" aria-hidden="true"><circle cx="15.5" cy="15.5" r="15.5" fill="var(--check)"/><path d="M9 16 L13.5 20.5 L22 11.5" fill="none" stroke="#fff" stroke-width="3" stroke-linecap="round" stroke-linejoin="round"/></svg>
      <span class="venue-label">Airport</span>
    </div>

    <div class="venue-tile col-1 row-3">
      <svg class="venue-icon" viewBox="0 0 60 60" aria-hidden="true" style="top:70px" fill="none" stroke="#fff" stroke-width="1.8" stroke-linejoin="round">
        <path d="M22 10 L14 13 L8 24 L15 28 L18 23 V52 H42 V23 L45 28 L52 24 L46 13 L38 10"/>
        <path d="M22 10 L30 18 L38 10"/><path d="M22 10 L26 20 L30 18 L34 20 L38 10"/>
        <path d="M29 19 L27 40 L30 44 L33 40 L31 19"/>
      </svg>
      <span class="venue-label two-line">Shopping<br>Center</span>
    </div>
  </section>

  <nav class="action-bar">
    <button class="action-button back-button">Back</button>
    <button class="action-button search-button">Search</button>
  </nav>
</main>
</body>
</html>
```